Wine Label front and back- Need to have an eye catching, classy wine label for restaurant placement.

label design for a wine label. eye catching for shelf placement. looking for simple and elegant label. Name of the vineyard will be the label recognition. Need back label to match with coloring and basic regulated info required by gov't (producer, address, and statement) Back label will be addressed after selected front label to match.
Will add $100 extra for the back label to match.

Target Market(s)

40-65 year old foodies

Colors
0355a3
eaf1f7

Requirements
Must have
• FERNHOLLOW (label name)
Estate,
Red Wine Blend NV,

```html
<!DOCTYPE html>
<html lang="en">
<head>
<meta charset="utf-8">
<title>Fernhollow Estate – Red Wine Blend NV</title>
<link rel="stylesheet" href="https://fonts.googleapis.com/css2?family=Playfair+Display:wght@700&family=Cormorant+Garamond:ital,wght@0,500;1,500&family=Josefin+Sans:wght@300&display=swap">
<style>
  :root {
    --brand-blue: #0355a3;
    --mist: #eaf1f7;
    --ink: #111111;
    --page: #ffffff;
  }
  html, body {
    margin: 0;
    width: 1200px;
    height: 1200px;
    overflow: hidden;
    background: var(--page);
  }
  .wine-label {
    position: absolute;
    left: 152px;
    top: 248px;
    width: 893px;
    height: 701px;
    background: var(--page);
    box-shadow: 0 0 14px rgba(0, 0, 0, 0.12);
    overflow: hidden;
  }
  .region-map {
    position: absolute;
    inset: 0;
    background: linear-gradient(180deg, var(--page) 0%, var(--mist) 100%);
  }
  .label-text {
    position: absolute;
    left: 0;
    width: 100%;
    margin: 0;
    text-align: center;
  }
  .brand-mark {
    position: absolute;
    left: 428px;
    top: 150px;
    width: 36px;
    height: 36px;
    border-radius: 50%;
    background: var(--brand-blue);
  }
  .vineyard-name {
    top: 218px;
    font-family: "Playfair Display", serif;
    font-weight: 700;
    font-size: 74px;
    line-height: 1;
    letter-spacing: 1px;
    color: var(--brand-blue);
  }
  .estate {
    top: 368px;
    font-family: "Cormorant Garamond", serif;
    font-weight: 500;
    font-size: 36px;
    line-height: 1;
    letter-spacing: 14px;
    text-indent: 14px;
    color: var(--ink);
  }
  .varietal {
    top: 447px;
    font-family: "Josefin Sans", sans-serif;
    font-weight: 300;
    font-size: 30px;
    line-height: 1;
    letter-spacing: 2px;
    color: var(--ink);
  }
  .alcohol {
    top: 560px;
    font-family: "Cormorant Garamond", serif;
    font-style: italic;
    font-weight: 500;
    font-size: 19px;
    line-height: 1;
    color: var(--ink);
  }
</style>
</head>
<body>
  <main class="wine-label">
    <div class="region-map" role="img" aria-label="Faint line map of the vineyard region with county borders and winding rivers"></div>
    <span class="brand-mark" aria-hidden="true"></span>
    <h1 class="label-text vineyard-name">FERNHOLLOW</h1>
    <p class="label-text estate">ESTATE</p>
    <p class="label-text varietal">RED WINE BLEND NV</p>
    <p class="label-text alcohol">Alc by Vol. 15.3%</p>
  </main>
</body>
</html>
```